The Book Cover for "Finding the Silver Lantern of Dawn" needs redesigned

First the back ground or art work needs to be replaced or redesigned.
The title Finding the Silver Lantern of Dawn needs to be redesigned so that the words "Finding the" is diminished in size compared to the rest of the title "Silver Lantern of Dawn"
The Sub-title "Tracing the forgotten path of the Evening Wind" needs to be more pronounced and readable.
The authors name needs to be downsized.

```html
<!DOCTYPE html>
<html lang="en">
<head>
<meta charset="utf-8">
<title>Finding the Silver Lantern of Dawn – Cover</title>
<link rel="stylesheet" href="https://fonts.googleapis.com/css2?family=Cormorant+Garamond:ital,wght@1,500;1,600&family=Montserrat:wght@800&display=swap">
<style>
  :root {
    --backdrop: #c9b9a6;
    --cover-black: #030507;
    --art-deep: #0b1724;
    --art-mid: #35617f;
    --art-light: #a9cbe2;
    --art-skin: #b7a7b4;
    --title-white: #ffffff;
    --subtitle-yellow: #f4e43a;
    --author-blue: #4aa6dc;
  }
  * { margin: 0; padding: 0; box-sizing: border-box; }
  html, body { width: 999px; height: 1200px; overflow: hidden; }
  body {
    background: var(--backdrop);
    display: flex;
    align-items: center;
    justify-content: center;
  }
  .book-cover {
    position: relative;
    width: 740px;
    height: 1110px;
    background: var(--cover-black);
    overflow: hidden;
  }
  .cover-art {
    position: absolute;
    left: 0; right: 0;
    top: 150px;
    height: 800px;
    background:
      radial-gradient(ellipse 38% 30% at 42% 30%, var(--art-skin) 0%, transparent 70%),
      radial-gradient(ellipse 30% 24% at 60% 66%, #c8bfc9 0%, transparent 70%),
      radial-gradient(ellipse 40% 45% at 85% 35%, var(--art-light) 0%, transparent 70%),
      radial-gradient(ellipse 60% 40% at 30% 80%, #9fb6c8 0%, transparent 75%),
      linear-gradient(160deg, var(--art-deep) 0%, var(--art-mid) 55%, var(--art-deep) 100%);
    -webkit-mask-image: linear-gradient(to bottom, transparent 0%, #000 14%, #000 78%, transparent 100%);
            mask-image: linear-gradient(to bottom, transparent 0%, #000 14%, #000 78%, transparent 100%);
  }
  .cover-title {
    position: absolute;
    top: 56px;
    left: 0; right: 0;
    text-align: center;
    color: var(--title-white);
    font-family: "Cormorant Garamond", Georgia, serif;
    font-style: italic;
    font-weight: 500;
    line-height: 1;
  }
  .title-lead { display: block; font-size: 44px; }
  .title-main { display: block; font-size: 74px; margin-top: 6px; }
  .cover-subtitle {
    position: absolute;
    left: 40px; right: 40px;
    bottom: 118px;
    text-align: center;
    color: var(--subtitle-yellow);
    font-family: "Cormorant Garamond", Georgia, serif;
    font-style: italic;
    font-weight: 600;
    font-size: 36px;
    line-height: 1.15;
  }
  .cover-author {
    position: absolute;
    left: 0; right: 0;
    bottom: 52px;
    text-align: center;
    color: var(--author-blue);
    font-family: "Montserrat", Arial, sans-serif;
    font-weight: 800;
    font-size: 36px;
    letter-spacing: 1px;
  }
</style>
</head>
<body>
  <main class="book-cover">
    <div class="cover-art" role="img" aria-label="Soft-lit scene of a young mother holding a sleeping baby among pale blue flowers"></div>
    <h1 class="cover-title">
      <span class="title-lead">Finding the</span>
      <span class="title-main">Silver Lantern of Dawn</span>
    </h1>
    <p class="cover-subtitle">Tracing the forgotten path of the Evening Wind</p>
    <p class="cover-author">RL FENN HARTWELL</p>
  </main>
</body>
</html>
```